VELA SKI Poster

Hello,
We are a small swiss ski brand, it is a ski de piste / ski on piste
We need a design for a small billboard/posters ( 180 H / 70 L CM )that will represent our brand.
The main goal is : visibility / promotion / lbrand and logo recognition
The design must be sporty, minimalistic ,elegant with a small accent of swiss alps/grauspitz
Our main target : high-end shops with luxurius sport brands. Good skiers, age 40 +
To get inspired by our "ambiance " please check our web-site :
https://vela-ski-demo.com/
instagram vela_ski
Other font styles liked:
- gotham

```html
<!DOCTYPE html>
<html lang="en">
<head>
<meta charset="utf-8">
<title>VELA SKI – Leave Your Own Track</title>
<link href="https://fonts.googleapis.com/css2?family=Teko:wght@500;600&family=Montserrat:wght@400;500&family=Tinos:ital,wght@1,700&display=swap" rel="stylesheet">
<style>
  :root {
    --stage: #e3e3e3;
    --paper: #f4f5f5;
    --paper-shade: #dfe2e3;
    --ink: #1d1d1f;
    --red: #e63a33;
    --white: #ffffff;
    --snow-light: #e9edf0;
    --snow-shade: #aebcc8;
  }
  * { margin: 0; padding: 0; box-sizing: border-box; }
  html, body {
    width: 1200px; height: 1084px; overflow: hidden;
    background: var(--stage);
  }
  .poster {
    position: absolute; left: 415px; top: 37px;
    width: 370px; height: 1010px; overflow: hidden;
    background: linear-gradient(160deg, var(--white) 0%, var(--paper) 45%, var(--paper-shade) 100%);
  }
  .poster-shapes { position: absolute; inset: 0; }
  .brand {
    position: absolute; top: 112px; left: 0; width: 100%;
    display: flex; justify-content: center; align-items: center; gap: 12px;
  }
  .brand-name {
    font-family: "Montserrat", sans-serif; font-weight: 500;
    font-size: 46px; letter-spacing: 1px; color: var(--ink);
  }
  .brand-square { width: 32px; height: 32px; background: var(--red); }
  .headline { font-size: 0; }
  .headline-accent {
    position: absolute; left: 89px; top: 244px; width: 154px; height: 6px;
    background: var(--red); transform: rotate(-1deg);
  }
  .headline-line {
    position: absolute; display: block; width: max-content; white-space: nowrap;
    font-family: "Teko", sans-serif; font-weight: 500;
    color: var(--white); line-height: 1; text-transform: uppercase;
    transform: rotate(-1.2deg);
  }
  .headline-line--top {
    left: 36px; top: 250px;
    background: var(--ink); font-size: 62px; padding: 12px 16px 4px 14px;
  }
  .headline-line--bottom {
    left: 91px; top: 320px;
    background: var(--red); font-size: 62px; padding: 10px 16px 2px 14px;
    box-shadow: -9px 9px 0 var(--ink);
  }
  .contact {
    position: absolute; top: 880px; left: 0; width: 100%;
    display: flex; flex-direction: column; align-items: center; gap: 12px;
  }
  .site-pill {
    width: 280px; height: 40px; border: 2px solid var(--white); border-radius: 20px;
    display: flex; align-items: center; justify-content: center; white-space: nowrap;
    font-family: "Montserrat", sans-serif; font-size: 14px; letter-spacing: 2.5px;
    color: var(--white); transform: rotate(-1deg);
  }
  .follow {
    display: flex; align-items: center; gap: 8px; color: var(--white);
    transform: rotate(-1deg); white-space: nowrap;
  }
  .follow-label { font-family: "Tinos", serif; font-style: italic; font-weight: 700; font-size: 17px; }
  .follow-dot { width: 12px; height: 12px; border-radius: 50%; background: var(--white); }
  .follow-handle { font-family: "Montserrat", sans-serif; font-size: 17px; }
</style>
</head>
<body>
  <main class="poster">
    <svg class="poster-shapes" width="370" height="1010" viewBox="0 0 370 1010">
      <defs>
        <linearGradient id="slope" x1="0" y1="0" x2="0" y2="1">
          <stop offset="0" stop-color="#6f8ea6"/>
          <stop offset="0.18" stop-color="var(--snow-light)"/>
          <stop offset="0.7" stop-color="#dde3e8"/>
          <stop offset="1" stop-color="var(--snow-shade)"/>
        </linearGradient>
      </defs>
      <polygon class="band-top" points="0,453 370,296 370,357 0,470" fill="var(--ink)"/>
      <polygon class="photo-area" points="0,460 370,355 370,742 0,842" fill="url(#slope)"
        role="img" aria-label="Photo of a skier carving down a groomed grauspitz piste beside two upright skis, one silver and one black"/>
      <polygon class="band-bottom" points="0,842 370,742 370,760 0,852" fill="var(--red)"/>
      <polygon class="band-bottom-dark" points="0,852 370,760 370,800 60,852" fill="var(--ink)"/>
      <polygon class="footer-field" points="0,852 60,852 370,800 370,1010 0,1010" fill="var(--red)"/>
    </svg>

    <header class="brand">
      <span class="brand-name">VELA SKI</span>
      <span class="brand-square"></span>
    </header>

    <h1 class="headline">
      <span class="headline-accent"></span>
      <span class="headline-line headline-line--top">Leave your</span>
      <span class="headline-line headline-line--bottom">Own track</span>
    </h1>

    <footer class="contact">
      <div class="site-pill">www.vela-ski-demo.com</div>
      <div class="follow">
        <span class="follow-label">Follow us on</span>
        <span class="follow-dot"></span>
        <span class="follow-handle">vela_ski</span>
      </div>
    </footer>
  </main>
</body>
</html>
```